Innovative cookies needs innovative design

We are launching some allergen friendly, vegan and sugar free biscuits, based on hemp, and we need a good label to go with it. More than the label itself is the concept that will then be adapted to all our brand.
If you're up for the challenge, to be part of something significant where to leave your blueprint on, show us what you've got!
Updates

Reason: some good things are coming up, there are some more designers that have saved the project to submit shortly, I would like to see more ideas coming out. So far brightquillworkshop is the one that has more elements we like, followed by elements used by Velto and Brix7waves. Once all designers have submitted we will have a picture big enough to decide who might be our first choice in following up on our re branding. Thanks all for your work.

Target Market(s)

Mums, fitness people, kids, vegan

Industry/Entity Type

Health Product

Font styles to use
Sans Serif
Decorative

Colors
9bcb3c
fbed22
ffc214
f78f20
ec1f27
add136
fbee3f
f04a50
ffcf3e

Requirements
Must have
• Must have a modern, Australian feel, with colours and key bullet points like:
• -100% allergen friendly (gluten, dairy, soy, nuts, eggs, sesame)
• -sugar free
• -school friendly
• -non gmo
• -paleo and vegan friendly
• -Made with organic millet and hemp protein
• Quite bold to understand and to catch attention.
Nice to have
• Some drawings, frames, arrows.
Should not have
• Not be boring.

```html
<!DOCTYPE html>
<html lang="en">
<head>
<meta charset="utf-8">
<title>Mira's Pantry – Biscuit Label</title>
<link rel="stylesheet" href="https://fonts.googleapis.com/css2?family=Anton&display=swap">
<style>
  :root {
    --page: #ffffff;
    --sun-yellow: #f4c145;
    --berry-red: #e5343f;
    --wave-line: #ece7f1;
    --claim-text: #e9e9ee;
    --claim-shadow: #3a1a1c;
    --brand-ink: #222022;
    --label-shadow: rgba(0, 0, 0, 0.45);
  }
  html, body {
    margin: 0;
    padding: 0;
    width: 1200px;
    height: 1000px;
    overflow: hidden;
    background: var(--page);
  }
  .canvas {
    position: relative;
    width: 1200px;
    height: 1000px;
  }
  .label {
    position: absolute;
    left: 18px;
    top: 245px;
    width: 1164px;
    height: 510px;
    background: var(--sun-yellow);
    box-shadow: 5px 7px 6px var(--label-shadow);
    overflow: hidden;
  }
  .label-wave {
    position: absolute;
    inset: 0;
    width: 100%;
    height: 100%;
  }
  .claims {
    position: absolute;
    left: 42px;
    top: 286px;
    margin: 0;
    padding: 0;
    list-style: none;
    font-family: "Anton", "Impact", sans-serif;
    font-size: 23px;
    line-height: 34px;
    letter-spacing: 0.2px;
    color: var(--claim-text);
    text-shadow: 2px 2px 0 var(--claim-shadow);
  }
  .brand {
    position: absolute;
    left: 800px;
    top: 215px;
    width: 340px;
    display: flex;
    align-items: center;
    justify-content: center;
    gap: 14px;
  }
  .brand-dot {
    width: 22px;
    height: 22px;
    border-radius: 50%;
    background: var(--brand-ink);
  }
  .brand-name {
    font-family: "Anton", "Impact", sans-serif;
    font-size: 52px;
    line-height: 1;
    color: var(--brand-ink);
    white-space: nowrap;
  }
</style>
</head>
<body>
  <main class="canvas">
    <section class="label">
      <svg class="label-wave" viewBox="0 0 1164 510" preserveAspectRatio="none" aria-hidden="true">
        <path d="M0 272 C 150 180, 300 92, 450 92 C 650 94, 800 222, 1164 236 L1164 510 L0 510 Z" fill="var(--berry-red)"/>
        <path d="M0 272 C 150 180, 300 92, 450 92 C 650 94, 800 222, 1164 236" fill="none" stroke="var(--wave-line)" stroke-width="6"/>
      </svg>

      <ul class="claims">
        <li>100% allergen friendly (gluten, dairy, soy, nuts, eggs, sesame)</li>
        <li>sugar free</li>
        <li>school friendly</li>
        <li>non gmo</li>
        <li>paleo and vegan friendly</li>
        <li>Made with organic millet and hemp protein</li>
      </ul>

      <div class="brand">
        <span class="brand-dot"></span>
        <span class="brand-name">Mira's Pantry</span>
      </div>
    </section>
  </main>
</body>
</html>
```